Onboarding Infographic/brochure

We are a small criminal defense firm looking to create some sort of infographic or brochure that we can onboard new clients with. We are currently sending it out via email but want something a bit cooler and fun to send to clients. The information is:

A Few Quick Rules

We are here to help each step of the way. While questions are never discouraged, this letter will answer some of the most common ones we get asked.

Communications

As a client, you should always be in the loop. While we will try to respond to questions as quickly as possible, sometimes we are unable to respond right away. Do not worry - we promise to get back to you soon. Some questions might take some time to research, and a correct answer is better than a quick one.

Appointments

One of the benefits of having an attorney is the ability to discuss your case outside of court, minus the stress and headaches. If you need an appointment, please contact the office.

Appointments must be scheduled in advance. We do not want you to make a special trip to the office only to learn that we are in court or otherwise unavailable.

Jail Visits

If your family member is currently in jail, we take that very seriously. We will visit your loved one and introduce ourselves. While the case is ongoing, we ask that a family member be designated a “contact” person so that messages can be relayed quickly. Never discuss the facts of the case over the phone with someone who is in jail. Jail calls are recorded and we have seen too many cases go south based on remarks made over recorded lines.

Police Reports and Discovery

We will do our best to provide you with copies of everything we receive on your case. Most information will be emailed, so please keep your email address up to date.

Changes in Contact Information

If you move or change numbers during the case, please let us know. It is difficult to help if we are unable to reach you, and helping you is why we are here.

Court Appearances

Cases do not get resolved as quickly as they do on television. Expect there to be several hearings in your case and it may be necessary for you to attend one or more of them. If a hearing is set, you will receive notice of the date and time of each hearing.

Billing and Collections

We understand that this investment was a huge decision for you. As we focus on providing the best representation, we will need for you to stay on schedule with any payment arrangements agreed to at the time of your initial consultation.

Again, thank you for your trust in us. We look forward to getting a fantastic outcome on your case.

Target Market(s)

Criminal defense clients and their families

Industry/Entity Type

Legal

Font styles to use
Serif

Requirements
Must have
• Must incorporate all of the rules we email out. Would like diagrams, images or pictures
Nice to have
• We attached a Welcome brochure. Not sure I want it to look super similar, hence the request for infographic.

```html
<!DOCTYPE html>
<html lang="en">
<head>
<meta charset="utf-8">
<title>Harbor Point Legal Group – A Few Quick Rules</title>
<link rel="stylesheet" href="https://fonts.googleapis.com/css2?family=Montserrat:wght@300;400;600;700&display=swap">
<style>
  :root {
    --backdrop: #636b78;
    --navy: #0d152b;
    --blue: #1793d8;
    --mist: #f0f1f3;
    --white: #ffffff;
    --ink: #0d152b;
    --body-grey: #5e636e;
    --body-light: #c4c8d2;
  }
  * { box-sizing: border-box; margin: 0; padding: 0; }
  html, body { width: 707px; height: 1200px; overflow: hidden; }
  body {
    background: var(--backdrop);
    font-family: "Montserrat", sans-serif;
    position: relative;
  }
  .page {
    position: absolute;
    left: 109px;
    width: 490px;
    height: 345px;
    overflow: hidden;
    background: var(--white);
    box-shadow: 0 6px 14px rgba(0,0,0,0.28);
  }
  .page--cover { top: 57px; }
  .page--inner { top: 428px; }
  .page--closing { top: 798px; }

  /* cover */
  .cover-photo {
    position: absolute; inset: 0;
    background:
      radial-gradient(ellipse at 80% 45%, rgba(210,170,140,0.55) 0%, rgba(210,170,140,0) 30%),
      linear-gradient(115deg, #ffffff 0%, #f4f6f9 35%, #a9c3dd 55%, #2c4f78 72%, #1a2b45 88%, #0f1a2c 100%);
  }
  .cover-panel {
    position: absolute; left: 0; top: 62px;
    width: 281px; height: 283px;
    background: var(--navy);
    padding: 0 0 0 45px;
  }
  .brand {
    position: absolute; left: 45px; top: 72px;
    display: flex; align-items: center; gap: 6px;
    color: var(--white);
    font-weight: 600; font-size: 10.5px; letter-spacing: 0.2px;
  }
  .brand-mark { width: 9px; height: 9px; background: var(--blue); }
  .cover-title {
    position: absolute; left: 45px; top: 114px;
    color: var(--white);
    font-weight: 700; font-size: 31px; line-height: 27px;
    letter-spacing: 0.3px;
  }
  .cover-intro {
    position: absolute; left: 45px; top: 186px; width: 185px;
    color: var(--body-light);
    font-weight: 300; font-size: 6.4px; line-height: 10.5px;
  }
  .cover-rule {
    position: absolute; left: 0; top: 307px;
    width: 100%; height: 5px; background: var(--blue);
  }

  /* sections */
  .block { position: absolute; }
  .block--mist { background: var(--mist); }
  .block--navy { background: var(--navy); }
  .rule-heading {
    position: relative;
    font-weight: 600; font-size: 12.3px; line-height: 14.5px;
    color: var(--ink);
    padding-left: 7px;
  }
  .rule-heading::before {
    content: ""; position: absolute; left: 0; top: 1px;
    width: 2px; height: 13px; background: var(--blue);
  }
  .rule-text {
    margin-top: 13px; padding-left: 7px;
    font-weight: 300; font-size: 6.4px; line-height: 10px;
    color: var(--body-grey);
  }
  .rule-text + .rule-text { margin-top: 10px; }
  .rule { position: absolute; width: 180px; }
  .block--navy .rule-heading { color: var(--white); }
  .block--navy .rule-text { color: var(--body-light); }

  .closing {
    position: absolute; left: 245px; top: 0; width: 245px; height: 345px;
    background: var(--navy);
    display: flex; flex-direction: column; align-items: center;
    padding-top: 116px;
    text-align: center;
  }
  .closing .brand { position: static; font-size: 8px; margin-bottom: 14px; }
  .closing-title { color: var(--white); font-weight: 700; font-size: 10.5px; }
  .closing-text {
    margin-top: 9px; width: 130px;
    color: var(--body-light);
    font-weight: 300; font-size: 6.4px; line-height: 10px;
  }
</style>
</head>
<body>

<section class="page page--cover">
  <div class="cover-photo" role="img" aria-label="Photo of two people in business suits shaking hands over a desk with charts and a pen"></div>
  <div class="cover-panel"></div>
  <div class="brand"><span class="brand-mark"></span>HARBOR POINT LEGAL GROUP</div>
  <h1 class="cover-title">A FEW<br>QUICK RULES</h1>
  <p class="cover-intro">We are here to help each step of the way. While questions are never discouraged, this letter will answer some of the most common ones we get asked.</p>
  <div class="cover-rule"></div>
</section>

<section class="page page--inner">
  <div class="block block--mist" style="left:245px;top:0;width:245px;height:285px;"></div>
  <div class="block block--navy" style="left:0;top:176px;width:245px;height:169px;"></div>

  <div class="rule" style="left:33px;top:34px;width:170px;">
    <h2 class="rule-heading">Communications</h2>
    <p class="rule-text">One of the benefits of having an attorney is the ability to discuss your case outside of court, minus the stress and headaches. If you need an appointment, please contact the office.</p>
    <p class="rule-text">Appointments must be scheduled in advance. We do not want you to make a special trip to the office only to learn that we are in court or otherwise unavailable.</p>
  </div>

  <div class="rule block--navy" style="left:33px;top:204px;width:175px;background:none;">
    <h2 class="rule-heading">Appointments</h2>
    <p class="rule-text">As a client, you should always be in the loop. While we will try to respond to questions as quickly as possible, sometimes we are unable to respond right away.</p>
    <p class="rule-text">Do not worry - we promise to get back to you soon. Some questions might take some time to research, and a correct answer is better than a quick one.</p>
  </div>

  <div class="rule" style="left:279px;top:34px;width:175px;">
    <h2 class="rule-heading">Jail Visits</h2>
    <p class="rule-text">If your family member is currently in jail, we take that very seriously. We will visit your loved one and introduce ourselves. While the case is ongoing, we ask that a family member be designated a “contact” person so that messages can be relayed quickly.</p>
    <p class="rule-text">Never discuss the facts of the case over the phone with someone who is in jail. Jail calls are recorded and we have seen too many cases go south based on remarks made over recorded lines.</p>
  </div>

  <div class="rule" style="left:279px;top:184px;width:165px;">
    <h2 class="rule-heading">Police Reports<br>&amp; Discovery</h2>
    <p class="rule-text">We will do our best to provide you with copies of everything we receive on your case. Most information will be emailed, so please keep your email address up to date.</p>
  </div>
</section>

<section class="page page--closing">
  <div class="block block--mist" style="left:0;top:0;width:245px;height:222px;"></div>

  <div class="rule" style="left:33px;top:32px;width:175px;">
    <h2 class="rule-heading">Court Appearances</h2>
    <p class="rule-text" style="margin-top:9px;">Cases do not get resolved as quickly as they do on television. Expect there to be several hearings in your case and it may be necessary for you to attend one or more of them. If a hearing is set, you will receive notice of the date and time of each hearing.</p>
  </div>

  <div class="rule" style="left:33px;top:127px;width:170px;">
    <h2 class="rule-heading">Changes in Contact<br>Information</h2>
    <p class="rule-text" style="margin-top:9px;">If you move or change numbers during the case, please let us know. It is difficult to help if we are unable to reach you, and helping you is why we are here.</p>
  </div>

  <div class="rule" style="left:29px;top:242px;width:175px;">
    <h2 class="rule-heading">Billing &amp; Collections</h2>
    <p class="rule-text" style="margin-top:9px;">We understand that this investment was a huge decision for you. As we focus on providing the best representation, we will need for you to stay on schedule with any payment arrangements agreed to at the time of your initial consultation.</p>
  </div>

  <div class="closing">
    <div class="brand"><span class="brand-mark"></span>HARBOR POINT LEGAL GROUP</div>
    <p class="closing-title">Thank you for your trust in us.</p>
    <p class="closing-text">We look forward to getting a fantastic outcome on your case.</p>
  </div>
</section>

</body>
</html>
```